Orthodontist Needs Promotional Discount Postcard

5.5 x 8.5 Horizontal 2-Sided Postcard for mailing.
Images & Logo on both sides okay; must be free stock Images from legit sources only, or use attached images. See our website for information, ShoreLaneSmiles.com
Context to include:
New Patient Special $500 off Braces or Clear Aligners
Cannot be combined with any other discounts.
Major dental insurance plans and Cara-Plan accepted
Affordable payment options are available
Call to schedule your free consultation
Present this new patient offer to receive your discount.
Offer ends January 31, 2022.
805-472-9186 www. ShoreLaneSmiles.com
462 N. Harlow Street, Suite B, Ventura, CA 93001-2718
office@shorelanesmiles.com

```html
<!DOCTYPE html>
<html lang="en">
<head>
<meta charset="utf-8">
<title>Shore Lane Smiles – New Patient Postcard</title>
<link rel="stylesheet" href="https://fonts.googleapis.com/css2?family=Ubuntu:wght@400;500;700&family=Questrial&display=swap">
<style>
  :root {
    --brand-blue: #1f9ad6;
    --slate: #6b6c70;
    --ink: #4a4a4d;
    --paper: #f4f4f4;
    --paper-warm: #ececec;
    --backdrop: #e4e4e4;
    --white: #ffffff;
    --rule: #8a8a8a;
  }
  * { box-sizing: border-box; margin: 0; padding: 0; }
  html, body { width: 1066px; height: 1200px; overflow: hidden; }
  body { background: var(--backdrop); position: relative; font-family: "Questrial", sans-serif; }
  p { white-space: nowrap; }

  .postcard {
    position: absolute; left: 174px; width: 730px; height: 472px;
    overflow: hidden; background: var(--paper);
    box-shadow: 0 10px 18px rgba(0,0,0,.18);
  }
  .postcard--front { top: 98px; }
  .postcard--back { top: 623px; background: var(--white); }

  .card-art { position: absolute; inset: 0; width: 100%; height: 100%; }

  /* brand mark */
  .brand { position: absolute; display: flex; align-items: center; color: var(--brand-blue); font-family: "Questrial", sans-serif; }
  .brand__dot { border-radius: 50%; background: var(--brand-blue); flex: none; }
  .brand__name { line-height: 1.1; text-transform: uppercase; white-space: nowrap; }
  .brand--front { left: 10px; top: 8px; width: 200px; flex-direction: column; text-align: center; }
  .brand--front .brand__dot { width: 62px; height: 62px; margin-bottom: 12px; }
  .brand--front .brand__name { font-size: 26px; letter-spacing: 1px; }
  .brand--back { left: 32px; top: 18px; gap: 16px; }
  .brand--back .brand__dot { width: 82px; height: 82px; }
  .brand--back .brand__name { font-size: 32px; letter-spacing: 1px; }

  /* front offer */
  .offer-badge {
    position: absolute; left: 351px; top: 263px; width: 343px; height: 112px;
    background: var(--brand-blue); border-radius: 10px;
    color: var(--white); font-family: "Ubuntu", sans-serif; font-weight: 700;
    text-align: center; padding-top: 10px; line-height: 1;
    box-shadow: 0 2px 6px rgba(0,0,0,.25);
  }
  .offer-badge__kicker { font-size: 26px; letter-spacing: .3px; }
  .offer-badge__amount { font-size: 35px; margin-top: 2px; }
  .offer-badge__item { font-size: 31px; margin-top: 2px; }

  .fine-print {
    position: absolute; left: 346px; width: 346px; top: 392px;
    color: var(--white); font-size: 14px; line-height: 17.5px; text-align: center;
  }

  /* back left panel */
  .info-panel { position: absolute; left: 0; top: 0; width: 366px; height: 284px; background: var(--paper-warm); overflow: hidden; }
  .cta {
    position: absolute; left: 0; width: 366px; top: 116px; text-align: center;
    font-family: "Ubuntu", sans-serif; font-weight: 500; color: var(--brand-blue);
    font-size: 15px; letter-spacing: -0.3px; line-height: 18px;
  }
  .cta__note { font-family: "Questrial", sans-serif; font-weight: 400; color: var(--ink); font-size: 13.5px; letter-spacing: 0; line-height: 16px; }
  .deadline {
    position: absolute; left: 13px; top: 156px; width: 344px; height: 32px;
    background: var(--brand-blue); color: var(--white);
    font-family: "Ubuntu", sans-serif; font-weight: 500; font-size: 19px; letter-spacing: -0.2px;
    display: flex; align-items: center; justify-content: center;
  }
  .contact { position: absolute; left: 0; width: 366px; top: 201px; text-align: center; color: var(--ink); }
  .contact__address { font-size: 12.5px; line-height: 16px; }
  .contact__lines { font-size: 15px; line-height: 19px; margin-top: 1px; }
  .contact__web { font-family: "Ubuntu", sans-serif; font-weight: 500; color: var(--brand-blue); font-size: 20px; letter-spacing: -0.3px; line-height: 26px; margin-top: 2px; }

  .aligner-photo { position: absolute; left: 0; top: 284px; width: 366px; height: 188px; }

  /* mailing side */
  .stamp-box { position: absolute; left: 609px; top: 31px; width: 91px; height: 96px; border: 1px solid #b5b5b5; }
  .address-block { position: absolute; left: 397px; top: 214px; width: 303px; }
  .address-block__label { font-family: "Ubuntu", sans-serif; font-weight: 500; font-size: 13px; color: #111; }
  .address-block__line { display: block; height: 37px; border-bottom: 1px solid var(--rule); }
  .address-block__line:first-of-type { height: 10px; }
</style>
</head>
<body>

<section class="postcard postcard--front" aria-label="Postcard front">
  <svg class="card-art" viewBox="0 0 730 472" preserveAspectRatio="none">
    <defs>
      <linearGradient id="smileTone" x1="0" y1="0" x2="1" y2="0.4">
        <stop offset="0" stop-color="#4a3424"/>
        <stop offset="0.4" stop-color="#2a1d15"/>
        <stop offset="0.75" stop-color="#a56e55"/>
        <stop offset="1" stop-color="#c08a6e"/>
      </linearGradient>
      <linearGradient id="slateBand" x1="0" y1="0" x2="0" y2="1">
        <stop offset="0" stop-color="#747579"/>
        <stop offset="1" stop-color="#5f6064"/>
      </linearGradient>
    </defs>
    <rect class="smile-photo" role="img" aria-label="Photo of a smiling woman with windswept hair" width="730" height="472" fill="url(#smileTone)"/>
    <path d="M0,196 C150,190 262,100 303,0 L312,0 C272,112 160,220 0,220 Z" fill="var(--brand-blue)"/>
    <path d="M0,0 H303 C262,100 150,190 0,196 Z" fill="var(--paper)"/>
    <path d="M0,322 C45,390 120,412 210,408 C360,400 500,330 730,316 V472 H0 Z" fill="url(#slateBand)"/>
    <path d="M40,378 C95,412 160,416 230,410 C380,398 520,330 730,316 V324 C520,338 380,408 230,418 C150,422 90,410 40,378 Z" fill="var(--brand-blue)"/>
  </svg>

  <div class="brand brand--front">
    <span class="brand__dot"></span>
    <span class="brand__name">Shore Lane<br>Smiles</span>
  </div>

  <div class="offer-badge">
    <p class="offer-badge__kicker">NEW PATIENT SPECIAL</p>
    <p class="offer-badge__amount">$500 OFF BRACES</p>
    <p class="offer-badge__item">OR CLEAR ALIGNERS</p>
  </div>

  <div class="fine-print">
    <p>Cannot be combined with any other discounts.</p>
    <p>Major dental insurance plans &amp; Cara-Plan accepted</p>
    <p>Affordable payment options are available</p>
  </div>
</section>

<section class="postcard postcard--back" aria-label="Postcard back">
  <div class="info-panel">
    <div class="brand brand--back">
      <span class="brand__dot"></span>
      <span class="brand__name">Shore Lane<br>Smiles</span>
    </div>

    <div class="cta">
      <p>CALL TO SCHEDULE YOUR FREE CONSULTATION</p>
      <p class="cta__note">Present this new patient offer to receive your discount.</p>
    </div>

    <p class="deadline">OFFER ENDS JANUARY 31, 2022</p>

    <div class="contact">
      <p class="contact__address">462 N. Harlow Street, Suite B, Ventura, CA 93001-2718</p>
      <p class="contact__lines">805-472-9186 | office@shorelanesmiles.com</p>
      <p class="contact__web">WWW.SHORELANESMILES.COM</p>
    </div>
  </div>

  <svg class="aligner-photo" viewBox="0 0 366 188" preserveAspectRatio="none" role="img" aria-label="Close-up photo of a clear aligner being fitted onto teeth">
    <defs>
      <linearGradient id="alignerTone" x1="0" y1="0" x2="0" y2="1">
        <stop offset="0" stop-color="#d9a597"/>
        <stop offset="0.35" stop-color="#eeeae4"/>
        <stop offset="0.7" stop-color="#c7b8b8"/>
        <stop offset="1" stop-color="#9c4a4c"/>
      </linearGradient>
    </defs>
    <rect width="366" height="188" fill="url(#alignerTone)"/>
  </svg>

  <div class="stamp-box" aria-label="Stamp area"></div>

  <div class="address-block">
    <p class="address-block__label">TO</p>
    <span class="address-block__line"></span>
    <span class="address-block__line"></span>
    <span class="address-block__line"></span>
    <span class="address-block__line"></span>
    <span class="address-block__line"></span>
  </div>
</section>

</body>
</html>
```